Dale Harwick Realtors
Stationary, Letterhead, Business Cards & Envelopes
Modern
Dale Harwick
Broker/ Owner
5817 Elmwood Crest Rd.
Fort Worth, Texas 76243
daleharwick@vesnamail.net
www.DaleHarwickRealtors.com
I would like the back to be the logo and I am not sure if it should have a white background or some color, I am open.
use logo here

```html
<!DOCTYPE html>
<html lang="en">
<head>
<meta charset="utf-8">
<title>Dale Harwick Realtors – Business Card</title>
<link href="https://fonts.googleapis.com/css2?family=Noto+Serif:wght@400;700&display=swap" rel="stylesheet">
<style>
  :root {
    --backdrop: #e9e6e1;
    --card: #ffffff;
    --navy: #1f3f8f;
    --navy-deep: #14296a;
    --swoosh: #3a3d45;
    --swoosh-soft: #b9bcc4;
    --ink: #2b2d33;
    --rule: #c9ccd3;
    --icon: #2e4e9e;
  }
  * { margin: 0; padding: 0; box-sizing: border-box; }
  html, body {
    width: 1200px; height: 780px; overflow: hidden;
    background: var(--backdrop);
    font-family: "Noto Serif", Georgia, serif;
  }
  .business-card {
    position: absolute; left: 100px; top: 104px;
    width: 1000px; height: 572px;
    background: var(--card);
    border-radius: 36px;
    overflow: hidden;
    box-shadow: 0 10px 30px rgba(0,0,0,0.18);
  }
  .card-header { position: absolute; inset: 0; width: 1000px; height: 572px; }
  .holder {
    position: absolute; right: 48px; top: 44px;
    text-align: right; color: #fff;
  }
  .holder-name { font-size: 38px; font-weight: 700; letter-spacing: 0.5px; }
  .holder-title { font-size: 24px; font-weight: 700; margin-top: 10px; }
  .brand {
    position: absolute; left: 70px; top: 340px;
    display: flex; flex-direction: column; align-items: center; gap: 22px;
  }
  .brand-square { width: 70px; height: 70px; background: var(--navy); }
  .brand-name {
    font-size: 40px; font-weight: 400; color: var(--navy-deep);
    letter-spacing: 1px; white-space: nowrap;
  }
  .divider {
    position: absolute; left: 522px; top: 270px;
    width: 2px; height: 240px; background: var(--rule);
  }
  .contact {
    position: absolute; left: 550px; top: 250px;
    color: var(--ink); font-size: 22px; line-height: 1.35;
  }
  .address { margin-bottom: 40px; }
  .contact-list { list-style: none; }
  .contact-list li { display: flex; align-items: center; gap: 14px; height: 34px; }
  .contact-list svg { width: 22px; height: 22px; flex: none; }
</style>
</head>
<body>
  <div class="business-card">
    <svg class="card-header" viewBox="0 0 1000 572" aria-hidden="true">
      <defs>
        <linearGradient id="bandFill" x1="0" y1="0" x2="1" y2="0">
          <stop offset="0" stop-color="#24479c"/>
          <stop offset="1" stop-color="#17307a"/>
        </linearGradient>
      </defs>
      <path d="M0 0 H1000 V150 Q560 200 0 250 Z" fill="url(#bandFill)"/>
      <path d="M0 250 Q560 200 1000 150 V168 Q560 222 0 262 Z" fill="var(--swoosh)"/>
      <path d="M0 262 Q560 222 1000 168 V178 Q560 236 0 270 Z" fill="var(--swoosh-soft)"/>
    </svg>

    <div class="holder">
      <div class="holder-name">Dale Harwick</div>
      <div class="holder-title">Broker / Owner</div>
    </div>

    <div class="brand">
      <div class="brand-square"></div>
      <div class="brand-name">Dale Harwick Realtors</div>
    </div>

    <div class="divider"></div>

    <div class="contact">
      <p class="address">5817 Elmwood Crest Rd.<br>Fort Worth, Texas 76243</p>
      <ul class="contact-list">
        <li>
          <svg viewBox="0 0 24 24"><path fill="var(--icon)" d="M6.6 10.8a15 15 0 0 0 6.6 6.6l2.2-2.2a1 1 0 0 1 1-.25 11.4 11.4 0 0 0 3.6.57 1 1 0 0 1 1 1V20a1 1 0 0 1-1 1A17 17 0 0 1 3 4a1 1 0 0 1 1-1h3.5a1 1 0 0 1 1 1c0 1.25.2 2.45.57 3.6a1 1 0 0 1-.25 1z"/></svg>
          <span>817-555-0142</span>
        </li>
        <li>
          <svg viewBox="0 0 24 24"><rect x="6" y="2" width="12" height="20" rx="2" fill="var(--icon)"/><rect x="8" y="5" width="8" height="11" fill="#fff"/><circle cx="12" cy="19" r="1.2" fill="#fff"/></svg>
          <span>817-555-0187</span>
        </li>
        <li>
          <svg viewBox="0 0 24 24"><rect x="2" y="5" width="20" height="14" rx="1.5" fill="var(--icon)"/><path d="M3 6.5 12 13l9-6.5" stroke="#fff" stroke-width="1.6" fill="none"/></svg>
          <span>daleharwick@vesnamail.net</span>
        </li>
        <li>
          <svg viewBox="0 0 24 24"><circle cx="12" cy="12" r="10" fill="var(--icon)"/><path d="M2 12h20M12 2c3 3 3 17 0 20M12 2c-3 3-3 17 0 20" stroke="#fff" stroke-width="1.3" fill="none"/></svg>
          <span>www.DaleHarwickRealtors.com</span>
        </li>
      </ul>
    </div>
  </div>
</body>
</html>
```